Business Card - Self Employed Director

My husband needs a business card design. 2 sided printing required.

He is self employed, in the vineyard management and renewable energy sectors (see below for more information) and design and accent colors should reflect this.

Design should be modern but classic and professional too.

Card to show personal contact information only. Exact information subject to confirmation on finalizing design as we are moving soon and need to confirm the exact details.

Dorian Feltsworth
email: dorian.feltsworth@brenquaystone.com
mobile: 021 064 51837
home: +64 (0) 3 4182 615
147 Harrow Fern Rise, RD4 Pellingham, Tarrowdale, NZ 7348

I like the attached design by Vexo for inspiration.

The reverse side should show name in bottom right corner with the pattern possibly reflecting renewable energy? Waves? Wind? Sea green, teal? Fresh, clean
Image on reverse should not be a photograph but a clean graphic based print on white background. Sans serfic fonts, Charcoal grey not black with accent colors reflected on the back?

Print ready artwork will be required. Please ask any questions :-) THANKS

Industry/Entity Type

Printing

Font styles to use
Sans Serif

Colors
86cfc6
ffffff
85abd2

Requirements
Must have
• Contact information as show
Should not have
• Anything cute, no red. No fancy flourish fonts.

```html
<!DOCTYPE html>
<html lang="en">
<head>
<meta charset="utf-8">
<title>Dorian Feltsworth — Business Card</title>
<link href="https://fonts.googleapis.com/css2?family=Roboto:wght@300;400&display=swap" rel="stylesheet">
<style>
  :root {
    --backdrop: #eceeef;
    --card: #ffffff;
    --charcoal: #4a4a4c;
    --body-grey: #6a6a6c;
    --divider: #d8d8d8;
    --sea-green: #86cfc6;
    --sky-blue: #85abd2;
  }
  * { margin: 0; padding: 0; box-sizing: border-box; }
  html, body {
    width: 1200px;
    height: 900px;
    overflow: hidden;
    background: var(--backdrop);
    font-family: "Roboto", "Helvetica Neue", Arial, sans-serif;
  }
  .canvas { position: relative; width: 1200px; height: 900px; }

  .card {
    position: absolute;
    left: 290px;
    width: 617px;
    height: 343px;
    background: var(--card);
    box-shadow: 0 1px 3px rgba(0,0,0,0.12);
    overflow: hidden;
  }
  .card--front { top: 87px; }
  .card--back  { top: 467px; }

  /* Front */
  .signature {
    position: absolute;
    right: 377px;
    top: 168px;
    text-align: right;
  }
  .signature__name {
    font-weight: 300;
    font-size: 22px;
    letter-spacing: -0.3px;
    color: var(--charcoal);
    line-height: 1;
    white-space: nowrap;
  }
  .signature__rule {
    margin-top: 5px;
    height: 2px;
    background: linear-gradient(90deg, var(--sea-green), var(--sky-blue));
  }
  .divider {
    position: absolute;
    left: 258px;
    top: 128px;
    width: 1px;
    height: 85px;
    background: var(--divider);
  }
  .contact {
    position: absolute;
    left: 279px;
    top: 126px;
    font-weight: 300;
    font-size: 13px;
    line-height: 17.4px;
    color: var(--body-grey);
    font-style: normal;
    white-space: nowrap;
  }

  /* Back */
  .wave-field {
    position: absolute;
    left: 0;
    top: 24px;
    width: 617px;
    height: 300px;
  }
  .signature--back {
    right: 20px;
    left: auto;
    top: 306px;
  }
  .signature--back .signature__name { font-size: 20px; }
</style>
</head>
<body>
<main class="canvas">

  <section class="card card--front" aria-label="Business card front">
    <div class="signature">
      <div class="signature__name">Dorian Feltsworth</div>
      <div class="signature__rule"></div>
    </div>
    <div class="divider"></div>
    <address class="contact">
      email: dorian.feltsworth@brenquaystone.com<br>
      mobile: 021 064 51837<br>
      home: +64 (0) 3 4182 615<br>
      147 Harrow Fern Rise, RD4 Pellingham,<br>
      Tarrowdale, NZ 7348
    </address>
  </section>

  <section class="card card--back" aria-label="Business card back">
    <svg class="wave-field" role="img" aria-label="Flowing translucent wave graphic in sea green and sky blue" viewBox="0 0 617 300" preserveAspectRatio="none">
      <defs>
        <linearGradient id="waveTone" x1="0" y1="0" x2="1" y2="0">
          <stop offset="0" stop-color="#86cfc6" stop-opacity="0.55"/>
          <stop offset="0.5" stop-color="#85abd2" stop-opacity="0.6"/>
          <stop offset="1" stop-color="#86cfc6" stop-opacity="0.65"/>
        </linearGradient>
        <linearGradient id="waveFade" x1="0" y1="0" x2="0" y2="1">
          <stop offset="0" stop-color="#fff" stop-opacity="0"/>
          <stop offset="0.15" stop-color="#fff" stop-opacity="1"/>
          <stop offset="0.85" stop-color="#fff" stop-opacity="1"/>
          <stop offset="1" stop-color="#fff" stop-opacity="0"/>
        </linearGradient>
        <mask id="waveMask">
          <rect width="617" height="300" fill="url(#waveFade)"/>
        </mask>
      </defs>
      <rect width="617" height="300" fill="url(#waveTone)" mask="url(#waveMask)"/>
    </svg>
    <div class="signature signature--back">
      <div class="signature__name">Dorian Feltsworth</div>
      <div class="signature__rule"></div>
    </div>
  </section>

</main>
</body>
</html>
```